Postcard design for accounting company

We need a postcard design (front and back) to our accounting firm that provides bookkeeping services to small and mid-size companies using LedgerPad Online. We would like to see designs that use the color blue and match our overall branding (see website). The final design should communicate professionalism, trust, and ease.

Target Market(s)

Small and Mid-Size companies

Industry/Entity Type

Accounting

Colors
0054AA
0677BA
7BADD7
CADEEF
E8F1F8

Requirements
Must have
• Logo, contact information, indicate services offered, color blue, and fit postcard template (see attached). Contact info = 555.318.2207, 1.800.555.0142, Info@BrightLedgerAccounting.com, www.BrightLedgerAccounting.com. Use the ZRPX Retail Indicia, which is a postage payment mark that takes the place of a regular postage stamp or meter stamp. Every ZRPX mailpiece must include the ZRPX Retail Indicia above and to the right of the address block. The ZRPX Retail Indicia does not have a specific size requirement but must be larger than 0.5" x 0.5". The type font must be in all caps and at least a 4 point size. It should fit in the area 1.625" from the right edge and 1.375" from top edge. Leave 1/8" of space around the top and right edge. See attached sample.
Nice to have
• Include that we a re Certified LedgerPad CertPartners (can include LPO logo). Also, maybe include the logos of the associations we are members of (North Pinecrest Chamber of Commerce, Federal Guild of Certified Ledgerkeepers, and Continental League of Female Enterprise Founders.

```html
<!DOCTYPE html>
<html lang="en">
<head>
<meta charset="utf-8">
<title>Bright Ledger Accounting Postcard</title>
<link href="https://fonts.googleapis.com/css2?family=Montserrat:wght@400;500;600;700;800&display=swap" rel="stylesheet">
<style>
  :root{
    --blue-deep:#0054AA;
    --blue-mid:#0677BA;
    --blue-bright:#1a6fd6;
    --blue-soft:#7BADD7;
    --blue-pale:#CADEEF;
    --blue-mist:#E8F1F8;
    --navy:#0b2a63;
    --ink:#2b2b2b;
    --grey-text:#555c66;
    --green:#3fb536;
    --bg:#d4d4d4;
    --white:#ffffff;
  }
  *{box-sizing:border-box;margin:0;padding:0}
  html,body{width:1200px;height:2602px;overflow:hidden}
  body{background:var(--bg);font-family:'Montserrat',sans-serif;position:relative}
  .postcard{position:absolute;left:137px;width:926px;height:630px;background:var(--white);box-shadow:0 14px 22px rgba(0,0,0,.35);overflow:hidden}
  .postcard--front{top:1015px}
  .postcard--back{top:1767px}
  .shapes{position:absolute;inset:0}
  .abs{position:absolute}
  .brand-name{left:56px;top:46px;width:290px;font-weight:700;font-size:30px;line-height:36px;color:var(--blue-deep)}
  .headline{left:50px;top:162px;color:var(--white);font-weight:800;font-size:36px;line-height:46px;letter-spacing:.5px}
  .subline{left:49px;top:252px;color:var(--white);font-size:20px;line-height:26px;font-weight:400;letter-spacing:.2px}
  .subline b{font-weight:700}
  .pill{left:47px;top:340px;width:390px;height:26px;border-radius:13px;background:var(--green);color:var(--white);font-weight:600;font-size:15px;line-height:26px;padding-left:36px}
  .pill::before{content:"";position:absolute;left:3px;top:2px;width:22px;height:22px;border-radius:50%;border:2px solid var(--white)}
  .packages-title{left:45px;top:392px;font-size:30px;font-weight:500;color:var(--grey-text);letter-spacing:1px}
  .packages-title strong{color:var(--blue-deep);font-weight:800}
  .services-tab{left:0;top:440px;width:35px;height:110px;background:var(--blue-deep);border-radius:0 8px 8px 0}
  .services-tab span{position:absolute;left:50%;top:50%;transform:translate(-50%,-50%) rotate(-90deg);color:var(--white);font-weight:600;font-size:17px;letter-spacing:1px}
  .checklist{list-style:none;font-size:15.5px;line-height:20px;color:var(--grey-text);font-weight:500}
  .checklist li{position:relative;padding-left:25px}
  .checklist li::before{content:"";position:absolute;left:2px;top:4px;width:12px;height:12px;border-radius:50%;background:var(--blue-deep)}
  .checklist li::after{content:"";position:absolute;left:5.5px;top:7px;width:5px;height:3px;border-left:1.6px solid var(--white);border-bottom:1.6px solid var(--white);transform:rotate(-45deg)}
  .list-a{left:51px;top:434px}
  .list-b{left:310px;top:434px}
  .contact-row{left:30px;right:26px;top:586px;display:flex;align-items:center;justify-content:space-between;color:var(--white);font-size:13.5px;font-weight:500;white-space:nowrap}
  .contact-item{display:flex;align-items:center;gap:6px}
  .sep{opacity:.9}
  .ico{width:18px;height:18px;flex:none}
  /* back */
  .section{left:42px;width:385px;color:var(--white)}
  .section h3{font-size:22px;font-weight:800;letter-spacing:.3px;display:flex;align-items:center;gap:8px;margin-bottom:6px}
  .section h3 .tick{width:18px;height:18px}
  .section p{font-size:14.5px;line-height:19px;font-weight:500}
  .sec-1{top:30px;width:395px}
  .sec-2{top:192px}
  .sec-3{top:336px;width:300px}
  .assoc-title{left:570px;top:40px;width:205px;text-align:center;color:var(--grey-text);font-size:15px;line-height:21px;font-weight:500}
  .badges{left:557px;top:92px;display:flex;gap:10px}
  .badge{width:46px;height:46px;border-radius:50%;background:var(--blue-mist);border:2px solid var(--blue-soft)}
  .badge--gold{border-color:#c9a34a;background:#fbf4e1}
  .badge--green{border-color:#3c8a3c;background:#e6f3e6}
  .badge--teal{border-color:#1c6b63;background:#e5f1ef}
  .indicia{left:787px;top:35px;width:112px;height:112px;border:1.5px solid var(--ink);text-align:center;font-size:13.5px;line-height:18.5px;font-weight:500;color:var(--ink);padding-top:9px}
  .back-contacts{left:40px;top:530px;color:#333;font-size:15.5px;font-weight:500;line-height:31px}
  .back-contacts div{display:flex;align-items:center;gap:6px}
  .back-contacts .ico{width:20px;height:20px}
  .back-contacts .hl{color:var(--blue-deep)}
  .faint-name{left:520px;top:505px;width:340px;font-size:38px;line-height:44px;font-weight:700;color:var(--blue-mist)}
</style>
</head>
<body>

<section class="postcard postcard--front">
  <svg class="shapes" width="926" height="630" viewBox="0 0 926 630">
    <defs>
      <linearGradient id="cityTone" x1="0" y1="0" x2="1" y2="1">
        <stop offset="0" stop-color="#0a3d8f"/><stop offset="1" stop-color="#061c45"/>
      </linearGradient>
      <linearGradient id="meetingTone" x1="0" y1="0" x2="1" y2="1">
        <stop offset="0" stop-color="#cfdbe9"/><stop offset=".5" stop-color="#8c9fb8"/><stop offset="1" stop-color="#dfe6ef"/>
      </linearGradient>
      <linearGradient id="deskTone" x1="0" y1="0" x2="1" y2="0">
        <stop offset="0" stop-color="#e9edf2"/><stop offset="1" stop-color="#c9d2dd"/>
      </linearGradient>
      <linearGradient id="chevTone" x1="0" y1="0" x2="0" y2="1">
        <stop offset="0" stop-color="#1684e0"/><stop offset="1" stop-color="#0054AA"/>
      </linearGradient>
    </defs>
    <polygon points="0,152 490,152 605,385 0,385" fill="url(#cityTone)" role="img" aria-label="Night city skyline in deep blue"/>
    <polygon points="565,0 926,0 926,392 650,392 520,100" fill="url(#meetingTone)" role="img" aria-label="Business team meeting around a table with laptops and charts"/>
    <polygon points="518,0 565,0 520,100 650,392 598,392 455,100" fill="url(#chevTone)"/>
    <polygon points="520,392 926,392 926,565 490,565" fill="url(#deskTone)" role="img" aria-label="Laptop on a desk showing an accounting dashboard"/>
    <rect x="0" y="565" width="926" height="65" fill="#2a2a2a"/>
    <polygon points="478,565 926,565 926,630 455,630" fill="var(--blue-deep)"/>
  </svg>

  <div class="abs brand-name">Bright Ledger Accounting</div>

  <h1 class="abs headline">ACCOUNTING<br>FOR YOUR BUSINESS</h1>
  <p class="abs subline"><b>Specializing</b> in Cloud-Based<br>Bookkeeping &amp; Payroll Processing with<br>LedgerPad Online by Numera.</p>
  <div class="abs pill">We a re Certified LedgerPad CertPartners</div>

  <h2 class="abs packages-title">BOOKKEEPING <strong>PACKAGES</strong></h2>
  <div class="abs services-tab"><span>SERVICES</span></div>
  <ul class="abs checklist list-a">
    <li>Accounts Receivable</li><li>Accounts Payable</li><li>Inventory</li><li>Payroll</li><li>Accruals/Adjusting Entries</li>
  </ul>
  <ul class="abs checklist list-b">
    <li>Account Reconciliation</li><li>Financial Reporting</li><li>Sales Tax</li><li>Consulting</li>
  </ul>

  <div class="abs contact-row">
    <span class="contact-item">
      <svg class="ico" viewBox="0 0 20 20"><circle cx="10" cy="10" r="9" fill="none" stroke="#fff" stroke-width="1.5"/><path d="M7 5.5l2 2-1 1.2c.6 1.3 1.6 2.3 2.8 2.9l1.2-1 2 2-1.2 1.4C9.5 13.8 6.2 10.5 5.6 7z" fill="#fff"/></svg>
      <span>555.318.2207</span>
    </span>
    <span class="sep">|</span>
    <span class="contact-item">
      <svg class="ico" viewBox="0 0 20 20"><circle cx="10" cy="10" r="9" fill="none" stroke="#fff" stroke-width="1.5"/><path d="M7 5.5l2 2-1 1.2c.6 1.3 1.6 2.3 2.8 2.9l1.2-1 2 2-1.2 1.4C9.5 13.8 6.2 10.5 5.6 7z" fill="#fff"/></svg>
      <span>1.800.555.0142</span>
    </span>
    <span class="sep">|</span>
    <span class="contact-item">
      <svg class="ico" viewBox="0 0 20 20"><circle cx="10" cy="10" r="9" fill="none" stroke="#fff" stroke-width="1.5"/><rect x="5.5" y="7" width="9" height="6.5" fill="none" stroke="#fff" stroke-width="1.2"/><path d="M5.5 7l4.5 3.5L14.5 7" fill="none" stroke="#fff" stroke-width="1.2"/></svg>
      <span>Info@BrightLedgerAccounting.com</span>
    </span>
    <span class="sep">|</span>
    <span class="contact-item">
      <svg class="ico" viewBox="0 0 20 20"><circle cx="10" cy="10" r="9" fill="none" stroke="#fff" stroke-width="1.5"/><circle cx="10" cy="10" r="5" fill="none" stroke="#fff" stroke-width="1.1"/><path d="M5 10h10M10 5v10" stroke="#fff" stroke-width="1.1"/></svg>
      <span>www.BrightLedgerAccounting.com</span>
    </span>
  </div>
</section>

<section class="postcard postcard--back">
  <svg class="shapes" width="926" height="630" viewBox="0 0 926 630">
    <defs>
      <linearGradient id="panelTone" x1="0" y1="0" x2="1" y2="1">
        <stop offset="0" stop-color="#0b56c2"/><stop offset=".6" stop-color="#0a4fb0"/><stop offset="1" stop-color="#0677BA"/>
      </linearGradient>
    </defs>
    <polygon points="0,0 545,0 350,505 0,505" fill="url(#panelTone)" role="img" aria-label="Blue-tinted office scene behind the service descriptions"/>
    <polygon points="455,0 545,0 500,118 420,0" fill="#1a7be0" opacity=".55"/>
  </svg>

  <div class="abs section sec-1">
    <h3><svg class="tick" viewBox="0 0 18 18"><circle cx="9" cy="9" r="8" fill="#fff"/><path d="M5 9.2l2.7 2.6L13 6.4" fill="none" stroke="#0a4fb0" stroke-width="2"/></svg>BOOKKEEPING</h3>
    <p>Let us take over the day to day bookkeeping so you can get back to running your business. We offer LedgerPad Online setup and ongoing bookkeeping, including daily journal entries, accounts payables &amp; receivables, bill pay, sales tax reporting &amp; payments, account reconciliation, and more.</p>
  </div>
  <div class="abs section sec-2">
    <h3><svg class="tick" viewBox="0 0 18 18"><circle cx="9" cy="9" r="8" fill="#fff"/><path d="M5 9.2l2.7 2.6L13 6.4" fill="none" stroke="#0a4fb0" stroke-width="2"/></svg>FINANCIAL REPORTING</h3>
    <p>We'll provide easy to understand financial reports that allow you and your team to manage cash flow, create budgets and make forecasting decisions.&nbsp; Want real time data?&nbsp; Let us provide solutions with the latest in mobile apps and dashboards.</p>
  </div>
  <div class="abs section sec-3">
    <h3><svg class="tick" viewBox="0 0 18 18"><circle cx="9" cy="9" r="8" fill="#fff"/><path d="M5 9.2l2.7 2.6L13 6.4" fill="none" stroke="#0a4fb0" stroke-width="2"/></svg>PAYROLL PROCESSING</h3>
    <p>We'll provide easy to understand financial reports that allow you and your team to manage cash flow, create budgets and make forecasting decisions.&nbsp; Want real time data? Let us provide solutions with the latest in mobile apps and dashboards.</p>
  </div>

  <div class="abs assoc-title">WE ARE ASSOCIATIONS<br>MEMBERS Of</div>
  <div class="abs badges">
    <div class="badge badge--green" role="img" aria-label="North Pinecrest Chamber of Commerce badge"></div>
    <div class="badge badge--gold" role="img" aria-label="Federal Guild of Certified Ledgerkeepers badge"></div>
    <div class="badge badge--teal" role="img" aria-label="Continental League of Female Enterprise Founders badge"></div>
    <div class="badge" role="img" aria-label="LedgerPad certified partner badge"></div>
  </div>

  <div class="abs indicia">PRSRT STD<br>WCRWSS<br>U.S.POSTAGE<br>PAID<br>ZRPX RETAIL</div>

  <div class="abs faint-name">Bright Ledger Accounting</div>

  <div class="abs back-contacts">
    <div>
      <svg class="ico" viewBox="0 0 20 20"><circle cx="10" cy="10" r="9" fill="none" stroke="#0054AA" stroke-width="1.5"/><path d="M7 5.5l2 2-1 1.2c.6 1.3 1.6 2.3 2.8 2.9l1.2-1 2 2-1.2 1.4C9.5 13.8 6.2 10.5 5.6 7z" fill="#0054AA"/></svg>
      <span>555.318.2207</span><span class="sep">|</span>
      <svg class="ico" viewBox="0 0 20 20"><circle cx="10" cy="10" r="9" fill="none" stroke="#0054AA" stroke-width="1.5"/><path d="M7 5.5l2 2-1 1.2c.6 1.3 1.6 2.3 2.8 2.9l1.2-1 2 2-1.2 1.4C9.5 13.8 6.2 10.5 5.6 7z" fill="#0054AA"/></svg>
      <span>1.800.555.0142</span>
    </div>
    <div>
      <svg class="ico" viewBox="0 0 20 20"><circle cx="10" cy="10" r="9" fill="none" stroke="#0054AA" stroke-width="1.5"/><rect x="5.5" y="7" width="9" height="6.5" fill="none" stroke="#0054AA" stroke-width="1.2"/><path d="M5.5 7l4.5 3.5L14.5 7" fill="none" stroke="#0054AA" stroke-width="1.2"/></svg>
      <span>Info@<span class="hl">BrightLedgerAccounting</span>.com</span>
    </div>
    <div>
      <svg class="ico" viewBox="0 0 20 20"><circle cx="10" cy="10" r="9" fill="none" stroke="#0054AA" stroke-width="1.5"/><circle cx="10" cy="10" r="5" fill="none" stroke="#0054AA" stroke-width="1.1"/><path d="M5 10h10M10 5v10" stroke="#0054AA" stroke-width="1.1"/></svg>
      <span>www.<span class="hl">BrightLedgerAccounting</span>.com</span>
    </div>
  </div>
</section>

</body>
</html>
```